Ad campaign in the solar industry

We are a young, up-and-coming solar module production company searching for a new print ad campaign. The design needs to express the core values of our company: a smart product, local support and service, as well as environmental awareness.
We would appreciate designs that communicate the advantages of renewable energy with a strong, clear message. Additionally, the concept should include visually appealing graphics to engage audiences throughout Europe and the US. Design concepts should be drafted in English. The design will appear in many forms; it will be adapted for publications, signage and online campaigns.
We value out-of-the box thinking, a modern approach, and creativity that goes beyond the usual solar ad.

```html
<!DOCTYPE html>
<html lang="en">
<head>
<meta charset="utf-8">
<title>Solvane – Greener. Smarter. Closer.</title>
<link href="https://fonts.googleapis.com/css2?family=Yanone+Kaffeesatz:wght@700&family=Audiowide&family=Arimo:wght@400;700&display=swap" rel="stylesheet">
<style>
:root{
  --green:#1f7a1f;
  --purple:#7a2a9a;
  --yellow:#f5c400;
  --orange:#f7a11a;
  --sun:#ffd21c;
  --brown:#7a3b33;
  --slate:#4a4a4a;
  --rule:#c8c8c8;
  --white:#ffffff;
  --ink:#111111;
  --lime:#8cff3a;
  --brand:#f08a1c;
}
*{box-sizing:border-box;margin:0;padding:0}
html,body{width:927px;height:1200px;overflow:hidden;background:var(--white)}
body{font-family:"Arimo",Arial,sans-serif;position:relative}
.ad{position:absolute;inset:0;width:927px;height:1200px;overflow:hidden}
.header{position:absolute;left:0;top:0;width:927px;height:98px;background:var(--white)}
.slogan{position:absolute;top:16px;font-family:"Yanone Kaffeesatz",sans-serif;font-weight:700;font-size:54px;letter-spacing:1px;text-shadow:1px 2px 2px rgba(0,0,0,.35)}
.slogan.greener{left:8px;color:var(--green)}
.slogan.smarter{left:216px;color:var(--purple)}
.slogan.closer{left:426px;color:var(--yellow)}
.brand-lockup{position:absolute;left:592px;top:4px;width:335px;height:92px}
.brand-mark{position:absolute;left:10px;top:8px;width:56px;height:56px;border-radius:50%;background:var(--brand)}
.brand-note{position:absolute;left:72px;top:24px;font-size:14px;color:var(--ink)}
.brand-name{position:absolute;left:62px;top:66px;font-size:18px;font-weight:700;color:var(--slate)}
.brand-tag{position:absolute;left:154px;top:66px;font-size:18px;color:#888}
.band{position:absolute;left:0;top:98px;width:927px;height:17px;background:var(--rule)}
.field{position:absolute;left:0;top:115px;width:927px;height:1085px;
  background:radial-gradient(circle at 22% 22%,var(--sun) 0,var(--orange) 55%,var(--sun) 100%)}
.panel{position:absolute;background:var(--brown);border:3px solid var(--white);border-radius:8px;color:var(--white)}
.panel h2{font-family:"Audiowide",sans-serif;font-weight:400;color:var(--sun);font-size:19px}
.intro{left:8px;top:137px;width:904px;height:113px;padding:8px 12px}
.intro p{font-weight:700;font-size:15.5px;line-height:21px;margin-top:5px}
.value{position:absolute;font-family:"Audiowide",sans-serif;color:var(--ink);line-height:1;
  text-shadow:0 0 3px var(--white),0 0 3px var(--white),0 0 5px var(--white)}
.value.quality{left:14px;top:264px;font-size:48px}
.value.pricing{left:398px;top:264px;font-size:21px;text-align:center}
.value.pricing span{display:block;font-size:29px;margin-top:5px}
.value.warranty{left:736px;top:264px;font-size:21px;text-align:center}
.value.warranty span{display:block;font-size:29px;margin-top:5px}
.value.safe{left:236px;top:342px;font-size:44px}
.value.reliable{left:536px;top:342px;font-size:44px}
.photo{position:absolute;border:3px solid var(--white)}
.photo.award{left:74px;top:415px;width:169px;height:172px;background:linear-gradient(160deg,#c9b9a0,#4a4a50)}
.photo.booth{left:267px;top:415px;width:234px;height:172px;background:linear-gradient(160deg,#e9e6c8,#7a8aa0)}
.photo.stand{left:77px;top:932px;width:232px;height:247px;background:linear-gradient(180deg,#7a7a7a,#e8e8e8 70%,#ffffff)}
.module{position:absolute;top:612px;height:233px;border:2px solid #222}
.module.m1{left:8px;width:144px;background:linear-gradient(160deg,#2c3260,#0e1126)}
.module.m2{left:168px;width:119px;background:linear-gradient(160deg,#2b2f3a,#0d0e12)}
.module.m3{left:301px;width:134px;background:linear-gradient(160deg,#3a6fc4,#1c3f86)}
.module.m4{left:449px;width:102px;background:linear-gradient(160deg,#2a2a2a,#0a0a0a)}
.promise{left:587px;top:405px;width:340px;height:316px;padding:8px 16px 0 14px}
.promise h2{font-size:20px}
.promise p{font-weight:700;font-size:15.5px;line-height:21px}
.promise .lead{margin-top:8px}
.promise ul{list-style:none;text-align:center;margin:5px 0 0;font-style:italic;font-size:15.5px;line-height:27px;color:var(--lime)}
.promise ul b{color:var(--sun)}
.contact{position:absolute;left:587px;top:742px;width:340px;height:152px;background:var(--slate);border:3px solid var(--white);color:var(--white);text-align:center;padding-top:6px}
.contact .co{font-family:"Audiowide",sans-serif;font-size:25px}
.contact p{font-weight:700;font-size:20px;line-height:25px}
.products{left:-3px;top:857px;width:570px;height:40px;padding:6px 12px;border-radius:0 8px 8px 0}
.products h2{font-size:20px}
.events{left:389px;top:912px;width:545px;height:283px;padding:4px 12px}
.events h2{font-size:21px}
.events p{font-weight:700;font-size:15.5px;margin-top:2px}
.schedule{margin-top:4px;width:497px;border-collapse:collapse;background:var(--white);color:var(--ink);font-size:12.5px}
.schedule th,.schedule td{border:1px solid #555;height:20px;padding:0 3px;text-align:left}
.schedule th{font-weight:700}
</style>
</head>
<body>
<main class="ad">
  <header class="header">
    <div class="slogan greener">GREENER.</div>
    <div class="slogan smarter">SMARTER.</div>
    <div class="slogan closer">CLOSER.</div>
    <div class="brand-lockup">
      <span class="brand-mark"></span>
      <span class="brand-note">LOGO PLACEHOLDER ONLY</span>
      <span class="brand-name">Solvane</span>
      <span class="brand-tag">Delivering safe solar</span>
    </div>
  </header>
  <div class="band"></div>
  <div class="field"></div>

  <section class="panel intro">
    <h2>Who is Solvane?</h2>
    <p>A leading international solar module developer and producer, offering the solar industry’s best quality / price ratio in the global PV market. Headquartered in Shanghai, we have offices throughout Asia, Europe and North America to support an international customer-base.</p>
  </section>

  <div class="value quality">Quality</div>
  <div class="value pricing">Competitive<span>Pricing</span></div>
  <div class="value warranty">World Class<span>Warranty</span></div>
  <div class="value safe">Safe</div>
  <div class="value reliable">Reliable</div>

  <div class="photo award" role="img" aria-label="Company representative holding a solar industry award"></div>
  <div class="photo booth" role="img" aria-label="Team toasting at the company exhibition booth"></div>

  <div class="module m1" role="img" aria-label="Dark blue solar module"></div>
  <div class="module m2" role="img" aria-label="Black monocrystalline solar module"></div>
  <div class="module m3" role="img" aria-label="Blue polycrystalline solar module"></div>
  <div class="module m4" role="img" aria-label="All-black solar module"></div>

  <section class="panel promise">
    <h2>Delivering Safe Solar</h2>
    <p class="lead">Our methods ensure the concept of "Safe Solar."</p>
    <ul>
      <li><b>Safe</b> source of Energy</li>
      <li><b>Safe</b> investment in a product<br>that is built to last 20+ years</li>
      <li><b>Safe</b> product with no moving parts,<br>and limited impact on the environment</li>
    </ul>
    <p>With its strong sales and technical support staff, Solvane is sure to deliver&nbsp; safe solar to their customers - each and every day.</p>
  </section>

  <address class="contact">
    <div class="co">Solvane</div>
    <p>1234 Streetname Ave.</p>
    <p>City, State 01234</p>
    <p>(123) 456 - 7890</p>
    <p>www.solvane.com</p>
  </address>

  <section class="panel products"><h2>Quality Products</h2></section>

  <div class="photo stand" role="img" aria-label="Flower arrangement on the company reception desk at a trade fair"></div>

  <section class="panel events">
    <h2>Learn More About Us In Person!</h2>
    <p>Visit the Solvane team at any of the following exhibitions.</p>
    <table class="schedule">
      <tr><th>Name</th><th>Date</th><th>City</th><th>Country</th><th>Booth No.</th></tr>
      <tr><td>THERMAFAIR</td><td>Feb 7-10</td><td>Paris</td><td>France</td><td>Hall 7.2, J58</td></tr>
      <tr><td>PV FAIR Tokyo</td><td>Feb 29 - Mar 2</td><td>Tokyo</td><td>Japan</td><td>E41-33</td></tr>
      <tr><td>ECOVISTA</td><td>Mar 15-18</td><td>Athens</td><td>Greece</td><td>Hall 4</td></tr>
      <tr><td>PV STATES</td><td>Mar 19-21</td><td>San Jose</td><td>USA</td><td>Booth #1015</td></tr>
      <tr><td>BUILDECO</td><td>Mar 20-22</td><td>London</td><td>UK</td><td>N3165</td></tr>
      <tr><td>CEF</td><td>Mar 29-31</td><td>Stuttgart</td><td>Germany</td><td>4E19</td></tr>
      <tr><td>EnV</td><td>Apr 3-5</td><td>Paris</td><td>France</td><td>Hall 1 Stand L33</td></tr>
      <tr><td>SOLARSHOW</td><td>May 9-11</td><td>Verona</td><td>Italy</td><td>Hall 6, E2.2</td></tr>
      <tr><td>SNPV</td><td>May 16-18</td><td>Shanghai</td><td>China</td><td>E1-550</td></tr>
      <tr><td>SUNFORUM</td><td>Jun 13-15</td><td>Munich</td><td>Germany</td><td>A3.360</td></tr>
    </table>
  </section>
</main>
</body>
</html>
```